UI/UX Re-Do for Velmora - a free to use project management platform for desktop and mobile.

UI/UX Re-Do for Velmora
Velmora is a free to use project management platform for desktop and mobile.
We are looking for help with our UI/UX re-design.
As of now the platform is totally functional.
The problem is around flow and look. We want VM to become something that any one can use to manage and even socialize any project. A project can be something work related like organizing a team around a software build, marketing campaign, shared client file space, etc... In fact, most of our current members are using VM for just such work projects.
We also see a project as planning a wedding, organizing a group trip, a simple to-do list, organizing a kids sports team, and so on...
To become a platform that people will use in their work and personal life we first need to become more intuitive and friendly - while maintaining advanced functionality for more advanced needs.
We need help to beautify, streamline, and simplify - while keeping all the functions.
The quickest way to understand VM, and our current issues is this short video:
https://vidshare-example.net/Kq8TzRw2mLp
For sure see this link for the entire most recent description AND images:
https://velmoraapp-example.com/?p=HtrwN4YcZsD
The best way to understand VM is to actually use it:
https://velmoraapp-example.com
Should you choose to take a run at improving VM here are the details:
Please focus your ideas for mobile, it's where we have the biggest issues.
Feel free to get outside the box.
Avoid swipe oriented designs.
Feel free to focus on ideas over polished outputs.
Use any tool you like, PS, hand drawing, written description if you think that works best.
(FYI - we use mostly use Google Presentation docs internally)
Point is illustration of ideas over tool choice.
Feel free to:
Create something totally new
And/or riff on what we have now
And/or riff on the new design we are considering (see images below)
|||
If we go the direction of the images/designs below the idea is to give people options on how they see/experience VM.
Just below is what we are calling Base Mode. This is a more basic and simple flow. Probably a default to keep new users feeling comfortable at the start.
<img src="https://img.picvault-example.net/8tqWLbN.jpg" style="width: 100%;">
https://img.picvault-example.net/8tqWLbN.jpg
|||
We are calling this optional view Atlas Mode. It is more advanced and can show all project, goal(renamed 'milestones') at the same time. This is more of a paint job on the current design.
<img src="https://img.picvault-example.net/mvdHRsJ.jpg" style="width: 100%;">
https://img.picvault-example.net/mvdHRsJ.jpg
|||
If you're submitting please let us know if you can also do the PS files for dev.
Not required, but once we nail down the concepts we want someone to hone in the PS files.
As an optional bonus we will also be giving credit to you/your company in VM.
Let us know if you do or don't want that.
We are excited to see your work!!
<img src=" " style="width: 100%;">
Target Market(s)
Anyone who needs to organize any project, big or small. The key is to make a super friendly user experience for new users while retaining advanced functions.

```html
<!DOCTYPE html>
<html lang="en">
<head>
<meta charset="utf-8">
<title>Velmora – Notes</title>
<link href="https://fonts.googleapis.com/css2?family=Poppins:wght@300;400;500;600&display=swap" rel="stylesheet">
<style>
:root{
  --bg:#f7f8fb;
  --topbar:#2a2f3d;
  --orange:#ff6b1a;
  --ink:#2b2f3a;
  --muted:#9a9ea8;
  --body:#6b7080;
  --line:#e8eaef;
  --white:#ffffff;
  --green:#4cc13d;
  --red:#f0284a;
  --pink:#ff5ec4;
  --link:#2a7de1;
  --icon:#c9ccd3;
}
*{box-sizing:border-box;margin:0;padding:0}
html,body{width:1200px;height:764px;overflow:hidden}
body{background:var(--bg);font-family:'Poppins',sans-serif;color:var(--ink);position:relative}
.abs{position:absolute}

/* top bar */
.topbar{position:absolute;left:0;top:0;width:1200px;height:71px;background:var(--topbar)}
.menu-icon{left:36px;top:27px}
.brand{left:89px;top:24px;color:var(--white);font-weight:600;font-size:17px;letter-spacing:.2px}
.search{left:673px;top:27px;display:flex;align-items:center;gap:12px;color:#9aa0ad;font-size:14px}
.bar-divider{left:940px;top:23px;width:1px;height:26px;background:#4a5060}
.user-photo{left:960px;top:13px;width:45px;height:45px;border-radius:50%;background:radial-gradient(circle at 50% 40%,#d9b8a0,#8a9aa8);border:2px solid #fff}
.user-name{left:1014px;top:25px;color:var(--white);font-size:14px;display:flex;align-items:center;gap:6px}
.view-toggle{left:1111px;top:27px}
.active-mark{left:1111px;top:0;width:21px;height:3px;background:var(--orange)}

/* left column */
.create-btn{left:89px;top:127px;width:332px;height:56px;background:var(--orange);border-radius:3px;color:#fff;font-size:11.5px;font-weight:500;display:flex;align-items:center;justify-content:center;letter-spacing:.2px}
.create-btn svg{position:absolute;right:16px;top:19px}
.umbrella{left:89px;width:332px;height:20px;display:flex;align-items:center;gap:8px;font-size:14px;color:var(--ink)}
.umbrella .dots{position:absolute;right:0}
.card{position:absolute;left:89px;width:332px;background:var(--white);border-radius:3px}
.card.open{box-shadow:0 20px 30px -12px rgba(40,50,80,.12)}
.project{position:relative;height:74px;padding:18px 0 0 22px}
.project.active{border-left:3px solid var(--orange);padding-left:19px;border-bottom:1px solid var(--line)}
.project h3{font-weight:400;font-size:16px;line-height:22px}
.status{font-size:10px;font-weight:500;letter-spacing:.3px;margin-top:3px}
.status.ok{color:var(--green)}
.status.late{color:var(--red)}
.goal{position:relative;height:71px;margin-left:40px;padding-top:18px}
.goal+.goal{border-top:1px solid var(--line)}
.goal h4{font-weight:400;font-size:12.5px;letter-spacing:.2px}
.row-tools{position:absolute;right:14px;top:30px;display:flex;align-items:center;gap:10px}
.goal .row-tools{top:27px}

/* right column */
.tabs{left:465px;top:123px;display:flex;gap:21px;font-size:13.5px;color:var(--muted)}
.tabs .current{color:var(--ink)}
.tab-line{left:465px;top:166px;width:646px;height:1px;background:var(--line)}
.tab-underline{left:465px;top:164px;width:43px;height:3px;background:var(--orange)}
.note{left:465px;top:198px;width:646px;height:566px;background:var(--white);border-radius:6px 6px 0 0}
.author-badge{left:28px;top:27px;width:45px;height:45px;border-radius:50%;background:var(--pink);color:#fff;font-size:16px;font-weight:500;display:flex;align-items:center;justify-content:center}
.author{left:82px;top:30px;font-size:14px}
.author small{display:block;font-size:11px;color:var(--muted);margin-top:2px}
.note-tools{right:20px;top:41px;display:flex;align-items:center;gap:10px}
.note-divider{left:0;top:96px;width:646px;height:1px;background:var(--line)}
.note-body{left:28px;top:130px;width:590px;font-size:13px;color:var(--body);line-height:28px}
.note-body p{margin-bottom:8px}
.note-body a{color:var(--link);text-decoration:none;line-height:20px;display:block;word-break:break-all}
.view-more{right:29px;top:361px;font-size:12.5px;color:var(--ink);display:flex;align-items:center;gap:5px}
.composer-line{left:0;top:505px;width:646px;height:1px;background:var(--line)}
.composer{left:28px;top:526px;font-size:13px;color:#b5b8c0}
.composer-tools{left:436px;top:526px;display:flex;gap:16px}
.send{left:575px;top:517px;width:38px;height:38px;border-radius:50%;background:var(--orange);display:flex;align-items:center;justify-content:center;box-shadow:0 6px 12px rgba(255,107,26,.3)}
</style>
</head>
<body>

<header class="topbar">
  <svg class="abs menu-icon" width="19" height="17" viewBox="0 0 19 17"><g stroke="#fff" stroke-width="2"><line x1="0" y1="1" x2="14" y2="1"/><line x1="0" y1="8" x2="19" y2="8"/><line x1="0" y1="15" x2="11" y2="15"/></g></svg>
  <div class="abs brand">Velmora</div>
  <div class="abs search">
    <svg width="15" height="15" viewBox="0 0 15 15"><circle cx="6" cy="6" r="5" fill="none" stroke="#9aa0ad" stroke-width="1.6"/><line x1="9.7" y1="9.7" x2="14" y2="14" stroke="#9aa0ad" stroke-width="1.6"/></svg>
    <span>Search here</span>
  </div>
  <div class="abs bar-divider"></div>
  <div class="abs user-photo" role="img" aria-label="User profile photo"></div>
  <div class="abs user-name">Marcus T. <svg width="8" height="5" viewBox="0 0 8 5"><path d="M1 1l3 3 3-3" fill="none" stroke="#fff" stroke-width="1.3"/></svg></div>
  <svg class="abs view-toggle" width="53" height="18" viewBox="0 0 53 18">
    <rect x="0" y="0" width="7" height="18" fill="#fff"/><rect x="9" y="0" width="13" height="18" fill="#fff"/>
    <rect x="31" y="0" width="6" height="18" fill="#5a606e"/><rect x="39" y="0" width="6" height="18" fill="#5a606e"/><rect x="47" y="0" width="6" height="18" fill="#5a606e"/>
  </svg>
  <div class="abs active-mark"></div>
</header>

<div class="abs create-btn">CREATE NEW UMBRELLA
  <svg width="17" height="17" viewBox="0 0 17 17"><g stroke="#fff" stroke-width="1.4"><line x1="8.5" y1="0" x2="8.5" y2="17"/><line x1="0" y1="8.5" x2="17" y2="8.5"/></g></svg>
</div>

<div class="abs umbrella" style="top:214px">
  <svg width="18" height="11" viewBox="0 0 18 11"><path d="M9 0C4.5 0 1.5 3 0 5.5 1.5 8 4.5 11 9 11s7.5-3 9-5.5C16.5 3 13.5 0 9 0z" fill="#2b2f3a"/><circle cx="9" cy="5.5" r="2.6" fill="#fff"/></svg>
  An Umbrella here
  <svg class="dots" width="4" height="16" viewBox="0 0 4 16"><g fill="#b5b8c0"><circle cx="2" cy="2" r="1.5"/><circle cx="2" cy="8" r="1.5"/><circle cx="2" cy="14" r="1.5"/></g></svg>
</div>

<div class="card" style="top:252px;height:72px">
  <div class="project">
    <h3>The Big Redesign</h3>
    <div class="status ok">STATUS</div>
    <div class="row-tools" style="top:27px">
      <svg width="18" height="11" viewBox="0 0 18 11"><path d="M9 0C4.5 0 1.5 3 0 5.5 1.5 8 4.5 11 9 11s7.5-3 9-5.5C16.5 3 13.5 0 9 0z" fill="#c9ccd3"/><circle cx="9" cy="5.5" r="2.6" fill="#fff"/></svg>
      <svg width="4" height="16" viewBox="0 0 4 16"><g fill="#b5b8c0"><circle cx="2" cy="2" r="1.5"/><circle cx="2" cy="8" r="1.5"/><circle cx="2" cy="14" r="1.5"/></g></svg>
    </div>
  </div>
</div>

<div class="card open" style="top:332px;height:216px">
  <div class="project active">
    <h3>UIX Design project</h3>
    <div class="status ok">STATUS</div>
    <div class="row-tools" style="top:28px">
      <svg width="18" height="11" viewBox="0 0 18 11"><path d="M9 0C4.5 0 1.5 3 0 5.5 1.5 8 4.5 11 9 11s7.5-3 9-5.5C16.5 3 13.5 0 9 0z" fill="#2b2f3a"/><circle cx="9" cy="5.5" r="2.6" fill="#fff"/></svg>
      <svg width="4" height="16" viewBox="0 0 4 16"><g fill="#b5b8c0"><circle cx="2" cy="2" r="1.5"/><circle cx="2" cy="8" r="1.5"/><circle cx="2" cy="14" r="1.5"/></g></svg>
    </div>
  </div>
  <div class="goal">
    <h4>GOAL 1 GOES HERE</h4>
    <div class="status late">STATUS</div>
    <div class="row-tools">
      <svg width="18" height="11" viewBox="0 0 18 11"><path d="M9 0C4.5 0 1.5 3 0 5.5 1.5 8 4.5 11 9 11s7.5-3 9-5.5C16.5 3 13.5 0 9 0z" fill="#c9ccd3"/><circle cx="9" cy="5.5" r="2.6" fill="#fff"/></svg>
      <svg width="4" height="16" viewBox="0 0 4 16"><g fill="#b5b8c0"><circle cx="2" cy="2" r="1.5"/><circle cx="2" cy="8" r="1.5"/><circle cx="2" cy="14" r="1.5"/></g></svg>
    </div>
  </div>
  <div class="goal">
    <h4>GOAL 2 GOES HERE</h4>
    <div class="status late">STATUS</div>
    <div class="row-tools">
      <svg width="18" height="11" viewBox="0 0 18 11"><path d="M9 0C4.5 0 1.5 3 0 5.5 1.5 8 4.5 11 9 11s7.5-3 9-5.5C16.5 3 13.5 0 9 0z" fill="#c9ccd3"/><circle cx="9" cy="5.5" r="2.6" fill="#fff"/></svg>
      <svg width="4" height="16" viewBox="0 0 4 16"><g fill="#b5b8c0"><circle cx="2" cy="2" r="1.5"/><circle cx="2" cy="8" r="1.5"/><circle cx="2" cy="14" r="1.5"/></g></svg>
    </div>
  </div>
</div>

<div class="abs umbrella" style="top:578px">
  <svg width="18" height="11" viewBox="0 0 18 11"><path d="M9 0C4.5 0 1.5 3 0 5.5 1.5 8 4.5 11 9 11s7.5-3 9-5.5C16.5 3 13.5 0 9 0z" fill="#c9ccd3"/><circle cx="9" cy="5.5" r="2.6" fill="#fff"/></svg>
  Lorem ipsum umbrella here
  <svg class="dots" width="4" height="16" viewBox="0 0 4 16"><g fill="#b5b8c0"><circle cx="2" cy="2" r="1.5"/><circle cx="2" cy="8" r="1.5"/><circle cx="2" cy="14" r="1.5"/></g></svg>
</div>
<div class="abs umbrella" style="top:623px">
  <svg width="18" height="11" viewBox="0 0 18 11"><path d="M9 0C4.5 0 1.5 3 0 5.5 1.5 8 4.5 11 9 11s7.5-3 9-5.5C16.5 3 13.5 0 9 0z" fill="#c9ccd3"/><circle cx="9" cy="5.5" r="2.6" fill="#fff"/></svg>
  Ipsum dolor Umbrella dec emit
  <svg class="dots" width="4" height="16" viewBox="0 0 4 16"><g fill="#b5b8c0"><circle cx="2" cy="2" r="1.5"/><circle cx="2" cy="8" r="1.5"/><circle cx="2" cy="14" r="1.5"/></g></svg>
</div>
<div class="abs umbrella" style="top:667px">
  <svg width="18" height="11" viewBox="0 0 18 11"><path d="M9 0C4.5 0 1.5 3 0 5.5 1.5 8 4.5 11 9 11s7.5-3 9-5.5C16.5 3 13.5 0 9 0z" fill="#c9ccd3"/><circle cx="9" cy="5.5" r="2.6" fill="#fff"/></svg>
  An aenean commodo Umbrella
  <svg class="dots" width="4" height="16" viewBox="0 0 4 16"><g fill="#b5b8c0"><circle cx="2" cy="2" r="1.5"/><circle cx="2" cy="8" r="1.5"/><circle cx="2" cy="14" r="1.5"/></g></svg>
</div>

<nav class="abs tabs">
  <span class="current">NOTES</span><span>PRESENTATION</span><span>STATUS</span><span>PEOPLE</span><span>FILES</span>
</nav>
<div class="abs tab-line"></div>
<div class="abs tab-underline"></div>

<section class="abs note">
  <div class="abs author-badge">VM</div>
  <div class="abs author">Dorian Fell VM Cases<small>6-1-2017 6:06 AM PKT</small></div>
  <div class="abs note-tools">
    <svg width="19" height="12" viewBox="0 0 18 11"><path d="M9 0C4.5 0 1.5 3 0 5.5 1.5 8 4.5 11 9 11s7.5-3 9-5.5C16.5 3 13.5 0 9 0z" fill="#2b2f3a"/><circle cx="9" cy="5.5" r="2.6" fill="#fff"/></svg>
    <svg width="4" height="16" viewBox="0 0 4 16"><g fill="#2b2f3a"><circle cx="2" cy="2" r="1.5"/><circle cx="2" cy="8" r="1.5"/><circle cx="2" cy="14" r="1.5"/></g></svg>
  </div>
  <div class="abs note-divider"></div>
  <div class="abs note-body">
    <p>Welcome to the Velmora 'Startup Starter Kit' - do more better!</p>
    <p>We recommend you look though the structure of this project as a an organizational logic, and then dig into some of the documentation templates.</p>
    <p>Best of luck on your venture, and please let us know if we can help!</p>
    <p style="margin-bottom:0">TMP - General Business Scrum Template</p>
    <a href="#">https://docs.sheetdesk-example.com/document/d/4hRQwLmZ8pTcVb k291Xn7d5Q2ys63n8KfpE4TRWg-qzL/edit</a>
  </div>
  <div class="abs view-more">
    <svg width="12" height="12" viewBox="0 0 12 12"><g stroke="#2b2f3a" stroke-width="1.2"><line x1="6" y1="0" x2="6" y2="12"/><line x1="0" y1="6" x2="12" y2="6"/></g></svg>VIEW MORE
  </div>
  <div class="abs composer-line"></div>
  <div class="abs composer">Type your message here</div>
  <div class="abs composer-tools">
    <svg width="18" height="17" viewBox="0 0 18 17"><path d="M9 1C4.6 1 1 3.9 1 7.5c0 2 1.1 3.7 2.8 4.9L3 16l4-2.2c.6.1 1.3.2 2 .2 4.4 0 8-2.9 8-6.5S13.4 1 9 1z" fill="#c9ccd3"/></svg>
    <svg width="18" height="18" viewBox="0 0 18 18"><g fill="none" stroke="#c9ccd3" stroke-width="2"><path d="M7.5 10.5l3-3"/><path d="M9 4.5l1.5-1.5a3 3 0 014.2 4.2L13 9"/><path d="M9 13.5L7.5 15a3 3 0 01-4.2-4.2L5 9"/></g></svg>
    <svg width="20" height="17" viewBox="0 0 20 17"><path d="M2 4h4l1.5-2.5h5L14 4h4v12H2z" fill="#c9ccd3"/><circle cx="10" cy="9.5" r="3.5" fill="#fff"/><circle cx="10" cy="9.5" r="2" fill="#c9ccd3"/></svg>
    <svg width="14" height="18" viewBox="0 0 14 18"><path d="M0 0h9l5 5v13H0z" fill="#c9ccd3"/><g stroke="#fff" stroke-width="1.2"><line x1="3" y1="8" x2="11" y2="8"/><line x1="3" y1="11" x2="11" y2="11"/><line x1="3" y1="14" x2="9" y2="14"/></g></svg>
  </div>
  <div class="abs send">
    <svg width="16" height="16" viewBox="0 0 16 16"><path d="M15 1L1 7l5 2 2 5z M6 9l9-8" fill="none" stroke="#fff" stroke-width="1.4" stroke-linejoin="round"/></svg>
  </div>
</section>

</body>
</html>
```